real esate business card with company logo and name

we need a business card design for a real esate company

The company name is Walsh & Brody Pty Ltd, and we have our logo designed and will upload. We want classic or moden feel. Black or white background. looks more textured. Should include folowinginformations
Paul Walsh and Lucy Brody
Sales Agents & Onsite Manager
p: 07 5948 2063
F: 07 5948 2174
M:0461 857 239
3/42 Marlin Crescent, KINGSLEY PARK QLD 4125

We want this business card looks professonal. Thank you in advance.

Industry/Entity Type

Real Estate Agent

Contact Information for Business Card

Paul Walsh and Lucy Brody
Onsite Manager & Sales Agents
p: 07 5948 2063
M:0461 857 239

Font styles to use
Serif

Colors
000000
fbfbfb
333333
959595

Requirements
Must have
• company logo and name, black or white back ground

```html
<!DOCTYPE html>
<html lang="en">
<head>
<meta charset="utf-8">
<title>Walsh &amp; Brody Pty Ltd — Business Card</title>
<link rel="stylesheet" href="https://fonts.googleapis.com/css2?family=Jost:wght@400;500;600&display=swap">
<style>
  :root {
    --ink: #000000;
    --paper: #fbfbfb;
    --charcoal: #333333;
    --silver: #959595;
    --card-light: #ececec;
    --backdrop: #e4e1dc;
  }
  * { box-sizing: border-box; margin: 0; padding: 0; }
  html, body {
    width: 1200px;
    height: 800px;
    overflow: hidden;
  }
  body {
    background: var(--backdrop);
    display: flex;
    align-items: center;
    justify-content: center;
    font-family: "Jost", sans-serif;
  }
  .business-card {
    position: relative;
    width: 900px;
    height: 480px;
    display: flex;
    border-radius: 10px;
    overflow: hidden;
    box-shadow: 0 14px 36px rgba(0, 0, 0, 0.22);
  }
  .brand-panel {
    position: relative;
    width: 370px;
    background:
      radial-gradient(circle at 40% 35%, #3a3a3a 0%, var(--charcoal) 55%, #232323 100%);
    display: flex;
    flex-direction: column;
    align-items: center;
    justify-content: center;
    gap: 22px;
    box-shadow: 4px 0 6px rgba(0, 0, 0, 0.25);
    z-index: 1;
  }
  .brand-texture {
    position: absolute;
    inset: 0;
    width: 100%;
    height: 100%;
    opacity: 0.35;
  }
  .brand-mark {
    position: relative;
    width: 64px;
    height: 64px;
    background: var(--silver);
  }
  .brand-name {
    position: relative;
    color: var(--silver);
    font-weight: 500;
    font-size: 20px;
    letter-spacing: 0.05em;
    text-transform: uppercase;
  }
  .contact-panel {
    flex: 1;
    background: linear-gradient(180deg, var(--paper) 0%, var(--card-light) 100%);
    color: var(--charcoal);
    display: flex;
    flex-direction: column;
    align-items: center;
    padding-top: 160px;
    text-align: center;
  }
  .agent-names {
    font-weight: 600;
    font-size: 25px;
    letter-spacing: 0.05em;
    text-transform: uppercase;
    color: var(--charcoal);
  }
  .agent-role {
    margin-top: 6px;
    font-size: 17px;
    color: var(--charcoal);
  }
  .contact-list {
    list-style: none;
    margin-top: 34px;
    font-size: 18px;
    line-height: 1.4;
    color: var(--charcoal);
  }
</style>
</head>
<body>
  <article class="business-card">
    <section class="brand-panel">
      <svg class="brand-texture" aria-hidden="true" viewBox="0 0 370 480" preserveAspectRatio="none">
        <filter id="grain">
          <feTurbulence type="fractalNoise" baseFrequency="0.9" numOctaves="2" stitchTiles="stitch"/>
          <feColorMatrix type="saturate" values="0"/>
        </filter>
        <rect width="370" height="480" filter="url(#grain)" opacity="0.4"/>
      </svg>
      <span class="brand-mark" aria-hidden="true"></span>
      <p class="brand-name">Walsh &amp; Brody Pty Ltd.</p>
    </section>
    <section class="contact-panel">
      <h1 class="agent-names">Paul Walsh and Lucy Brody</h1>
      <p class="agent-role">Onsite Manager &amp; Sales Agents</p>
      <ul class="contact-list">
        <li>p: 07 5948 2063</li>
        <li>F: 07 5948 2174</li>
        <li>M:0461 857 239</li>
        <li>3/42 Marlin Crescent, KINGSLEY PARK QLD 4125</li>
      </ul>
    </section>
  </article>
</body>
</html>
```